New Business Card/Website Logo

We need a business card design for a new company based in Sydney. The company focuses mainly in construction in the field of form work and concreting. Attached is the logo being used already which can be used as a base for a new design, the current one is simply too bland and we are looking to spruce it up so it stands out and looks nicer. The logo would also be used on the website which is currently under construction. The attached image has the name, mobile and also the license number which needs to be there. The current email address on there can be removed and can be replaced with the website http://www.bravelintel.com.au, thanks!
Updates

Target Market(s)

Construction industry. Focusing on form work and concreting

Industry/Entity Type

Construction

Requirements
Must have
• License # on card along with website http://www.bravelintel.com.au and mobile phone number
Nice to have
• You have freedom with the design. The current design was a mock up done quite quickly. Please just keep in mind the target audience - construction, thanks.
Should not have
• the mailvista email address can be removed(refer picture) and replaced somewhere on the design with the website http://www.bravelintel.com.au

```html
<!DOCTYPE html>
<html lang="en">
<head>
<meta charset="utf-8">
<title>Bravelintel Business Card</title>
<link rel="stylesheet" href="https://fonts.googleapis.com/css2?family=Arimo:wght@400;700&display=swap">
<style>
  :root {
    --backdrop: #2b2725;
    --card: #f3f3f3;
    --ink: #1f2d3a;
    --text: #2a2a2a;
    --green: #2db34a;
    --divider: #8a8f94;
  }
  * { margin: 0; padding: 0; box-sizing: border-box; }
  html, body {
    width: 1200px;
    height: 900px;
    overflow: hidden;
    background: var(--backdrop);
    font-family: "Arimo", Arial, sans-serif;
  }
  .business-card {
    position: absolute;
    left: 100px;
    top: 160px;
    width: 1000px;
    height: 579px;
    background: var(--card);
    overflow: hidden;
  }
  .brand {
    position: absolute;
    left: 77px;
    top: 80px;
    display: flex;
    align-items: center;
    gap: 26px;
  }
  .brand-square {
    width: 58px;
    height: 58px;
    background: var(--ink);
  }
  .brand-name {
    font-size: 74px;
    font-weight: 700;
    color: var(--ink);
    letter-spacing: 1px;
    line-height: 1;
  }
  .pointer {
    position: absolute;
    left: 0;
    top: 349px;
  }
  .holder {
    position: absolute;
    left: 77px;
    top: 345px;
  }
  .holder-name {
    font-size: 41px;
    font-weight: 700;
    color: var(--ink);
    line-height: 1.1;
  }
  .holder-role {
    font-size: 30px;
    color: var(--green);
    line-height: 1.2;
  }
  .column-divider {
    position: absolute;
    left: 456px;
    top: 288px;
    width: 2px;
    height: 203px;
    background: linear-gradient(to bottom, transparent, var(--divider) 20%, var(--divider) 80%, transparent);
  }
  .contact {
    position: absolute;
    left: 507px;
    top: 318px;
    width: 420px;
    color: var(--text);
    font-size: 29px;
  }
  .licence {
    padding-bottom: 10px;
    border-bottom: 2px dashed var(--green);
    margin-bottom: 14px;
  }
  .contact-line {
    display: flex;
    align-items: center;
    gap: 12px;
    line-height: 1.45;
  }
  .contact-line svg { flex: none; }
  .footer-bands {
    position: absolute;
    left: 0;
    bottom: 0;
  }
</style>
</head>
<body>
  <main class="business-card">
    <div class="brand">
      <span class="brand-square"></span>
      <span class="brand-name">BRAVELINTEL</span>
    </div>

    <svg class="pointer" width="46" height="68" viewBox="0 0 46 68">
      <polygon points="0,0 46,34 0,68" fill="var(--green)"/>
    </svg>

    <div class="holder">
      <p class="holder-name">Marco Ellison</p>
      <p class="holder-role">Occupation</p>
    </div>

    <div class="column-divider"></div>

    <div class="contact">
      <p class="licence">Licence: 384915B</p>
      <p class="contact-line">
        <svg width="26" height="26" viewBox="0 0 24 24" aria-hidden="true">
          <path fill="var(--ink)" d="M6.6 10.8a15.1 15.1 0 0 0 6.6 6.6l2.2-2.2c.3-.3.7-.4 1-.2 1.1.4 2.3.6 3.6.6.6 0 1 .4 1 1V20c0 .6-.4 1-1 1A17 17 0 0 1 3 4c0-.6.4-1 1-1h3.5c.6 0 1 .4 1 1 0 1.3.2 2.5.6 3.6.1.3 0 .7-.2 1z"/>
        </svg>
        0412 508 937
      </p>
      <p class="contact-line">
        <svg width="26" height="26" viewBox="0 0 24 24" aria-hidden="true" fill="none" stroke="var(--ink)" stroke-width="1.8">
          <circle cx="12" cy="12" r="9"/>
          <ellipse cx="12" cy="12" rx="4" ry="9"/>
          <line x1="3" y1="12" x2="21" y2="12"/>
          <path d="M5 7h14M5 17h14"/>
        </svg>
        www.bravelintel.com.au
      </p>
    </div>

    <svg class="footer-bands" width="1000" height="26" viewBox="0 0 1000 26">
      <polygon points="0,0 443,0 432,26 0,26" fill="var(--ink)"/>
      <polygon points="455,0 1000,0 1000,26 444,26" fill="var(--green)"/>
    </svg>
  </main>
</body>
</html>
```